Lend a Lantern Website Design (design layout only)

We need a website design for a new nonprofit organization based in Des Moines, Iowa called Lend a Lantern. The nonprofit provides soccer training opportunities to youth soccer players looking to improve their game while also affecting the lives of the less fortunate in a positive way. While participating in the training programs the players also go out and raise money for selected charities. The organization then donates the funds. In its first 18 months we donated $10,500. We would like to see designs attempt to symbolize the mission of the nonprofit - essentially "improve you while improving someone else."

We would like to see the following features:

· A place to donate - Our intent is to have the home page linked to the donation page; a simple straight-forward process for people to give money, and make donating as painless as possible - no account needed to make a donation, credit card or e-check should be the only information needed to donate, and have it be on a single page.

· A photo gallery so people can browse the photo gallery to get a better understanding of our organization and a place to add videos and a calendar to show upcoming events

· A place for contact information and the profiles of directors and board members. This should include a spot showing all the charities the organization donates to. Also includes a news section/blog for comments and suggestions.

We want the design to revolve around the content and mission. We would really like to stress our organization as nonprofit. We would also like if the website was user friendly and easy to navigate.

The logo of our organization is uploaded

```html
<!DOCTYPE html>
<html lang="en">
<head>
<meta charset="utf-8">
<title>Lend a Lantern</title>
<link rel="stylesheet" href="https://fonts.googleapis.com/css2?family=Montserrat:wght@400;600;700&family=Open+Sans:wght@400;600&display=swap">
<style>
:root{
  --green:#7ba556;
  --green-dark:#2d4a1b;
  --navy:#2a3043;
  --ink:#222;
  --muted:#666;
  --line:#e2e2e2;
  --panel:#f4f4f4;
  --footer:#1f1f1f;
  --white:#fff;
}
*{box-sizing:border-box;margin:0;padding:0}
html,body{width:904px;height:1200px;overflow:hidden;background:var(--white)}
body{position:relative;font-family:"Open Sans",sans-serif;color:var(--ink)}
.abs{position:absolute}

/* hero */
.hero{left:0;top:0;width:904px;height:530px;
  background:radial-gradient(ellipse at 45% 45%,#6b2f3c 0%,#3d2d40 35%,#2a3043 75%);}
.hero-shade{left:0;top:0;width:904px;height:530px;background:rgba(30,35,55,.35)}
.brand{left:70px;top:0;width:95px;height:86px;background:var(--white);border-radius:0 0 10px 10px;
  display:flex;align-items:center;justify-content:center;text-align:center;
  font-family:"Montserrat",sans-serif;font-weight:700;font-size:13px;line-height:1.15;color:var(--green)}
.btn-online{left:695px;top:18px;width:139px;height:32px;background:var(--green);color:var(--white);
  border-radius:3px;font-family:"Montserrat",sans-serif;font-size:11.5px;display:flex;align-items:center;justify-content:center}
.nav{top:74px;right:68px;display:flex;gap:0;align-items:center;font-family:"Montserrat",sans-serif;font-size:10px;color:var(--white)}
.nav span{padding:4px 12.5px}
.nav .active{background:var(--green);border-radius:2px;margin-right:1px}
.hero-rule{left:72px;top:117px;width:763px;height:1px;background:rgba(255,255,255,.45)}
.hero-title{left:0;top:168px;width:904px;text-align:center;color:var(--white);
  font-family:"Montserrat",sans-serif;font-weight:700;font-size:39px;line-height:45px}
.hero-sub{left:0;top:322px;width:904px;text-align:center;color:var(--white);
  font-family:"Montserrat",sans-serif;font-weight:600;font-size:17.5px;line-height:21px;letter-spacing:2px}
.btn-hero{top:396px;width:176px;height:38px;border-radius:3px;color:var(--white);
  font-family:"Montserrat",sans-serif;font-weight:600;font-size:12.5px;letter-spacing:1px;display:flex;align-items:center;justify-content:center}
.btn-dark{left:250px;background:#14161c;border:1px solid #3a3d46}
.btn-green{left:452px;background:var(--green)}

/* donation */
.donate{left:70px;top:556px;width:384px;height:270px;background:var(--panel);border:1px solid var(--line)}
.donate h2{position:absolute;left:9px;top:12px;font-family:"Montserrat",sans-serif;font-weight:400;font-size:16px}
.donate .req{position:absolute;right:14px;top:18px;font-size:9px}
.donate .sep{position:absolute;left:9px;top:38px;width:362px;height:1px;background:var(--line)}
.lbl{position:absolute;font-size:9px;color:var(--ink)}
.field{position:absolute;height:22px;background:#ebebeb;border:1px solid #ddd}
.select{position:absolute;height:22px;background:#ebebeb;border:1px solid #ddd;font-size:9px;color:#444;padding:5px 7px}
.select i{position:absolute;right:0;top:0;width:25px;height:20px;background:var(--green-dark)}
.select i:after{content:"";position:absolute;left:8px;top:8px;border:4px solid transparent;border-top:5px solid var(--white)}
.radios{position:absolute;left:12px;top:122px;display:flex;gap:13px;font-size:9px;color:#666}
.radios span:before{content:"";display:inline-block;width:7px;height:7px;border:1px solid #ccc;border-radius:50%;margin-right:6px;vertical-align:-1px}
.ccv-help{position:absolute;left:86px;top:224px;font-size:7.5px;color:#666;line-height:11px}
.ccv-help u{color:#555}

/* about */
.about-title{left:475px;top:551px;font-family:"Montserrat",sans-serif;font-size:19px;font-weight:400}
.about-photo{left:475px;top:585px;width:359px;height:129px;background:linear-gradient(180deg,#3c4f8a 0%,#5a6aa0 40%,#4e8a3a 65%,#3f7a2e 100%)}
.about-text{left:475px;top:724px;width:362px;font-size:8.5px;line-height:12.5px;color:#555}
.btn-small{height:22px;width:108px;background:var(--green-dark);color:var(--white);font-size:9.5px;
  display:flex;align-items:center;justify-content:center;gap:7px}
.btn-small svg{width:11px;height:11px}

/* cards */
.card-photo{top:886px;height:113px}
.card-title{top:1011px;width:236px;text-align:center;font-family:"Montserrat",sans-serif;font-size:14px}
.card-text{top:1038px;width:236px;text-align:center;font-size:8.5px;line-height:14px;color:#777}

/* footer */
.footer{left:0;top:1172px;width:904px;height:28px;background:var(--footer);color:#ddd;font-size:8.5px}
.footer .copy{position:absolute;left:71px;top:8px}
.footer .links{position:absolute;right:69px;top:8px}
</style>
</head>
<body>

<header>
  <div class="abs hero" role="img" aria-label="Youth soccer team in red kits huddled together on a pitch"></div>
  <div class="abs hero-shade"></div>
  <div class="abs brand">Lend a<br>Lantern</div>
  <div class="abs btn-online">Online Transaction</div>
  <nav class="abs nav">
    <span class="active">HOME</span><span>ABOUT US</span><span>TEAM</span><span>HELP</span><span>LEAD</span><span>GALLERY</span><span style="padding-right:0">CONTACT US</span>
  </nav>
  <div class="abs hero-rule"></div>
  <h1 class="abs hero-title">The nonprofit<br>provides soccer<br>training opportunities</h1>
  <p class="abs hero-sub">Lorem ipsum dolar sit amet is dummy<br>languuange</p>
  <div class="abs btn-hero btn-dark">Read More</div>
  <div class="abs btn-hero btn-green">+ Get Started Now</div>
</header>

<section class="abs donate">
  <h2>Donation Details</h2>
  <span class="req">Lorem ipsum dolor *</span>
  <div class="sep"></div>
  <span class="lbl" style="left:10px;top:51px">Donation Amount *</span>
  <div class="select" style="left:10px;top:64px;width:197px">$0.00 Per month<i></i></div>
  <span class="lbl" style="left:10px;top:108px">Select your credit card type *</span>
  <div class="radios"><span>Mintcard</span><span>Amplex</span><span>Dinerly</span></div>
  <span class="lbl" style="left:10px;top:152px">Name on card *</span>
  <div class="field" style="left:10px;top:166px;width:171px"></div>
  <span class="lbl" style="left:199px;top:154px">Credit card number *</span>
  <div class="field" style="left:199px;top:166px;width:171px"></div>
  <span class="lbl" style="left:11px;top:206px">CCV number *</span>
  <div class="field" style="left:10px;top:224px;width:73px"></div>
  <div class="ccv-help">What is CCV ?<br><u>Click here</u></div>
  <span class="lbl" style="left:172px;top:208px">Expiry date *</span>
  <div class="select" style="left:172px;top:226px;width:87px">Jan<i></i></div>
  <div class="select" style="left:283px;top:226px;width:87px">2014<i></i></div>
</section>

<section>
  <h2 class="abs about-title">About Lend a Lantern</h2>
  <div class="abs about-photo" role="img" aria-label="Young player leaping to kick a soccer ball on grass"></div>
  <p class="abs about-text">Sed ut perspiciatis unde omnis iste natus error sit voluptatem accusantium doloremque laudantium, totam rem aperiam, eaque ipsa quae ab illo inventore veritatis et quasi architecto beatae vitae dicta sunt explicabo. Nemo enim ipsam voluptatem quia voluptas sit aspernatur aut odit aut fugit, sed quia consequuntur magni dolores eos qui ratione voluptatem sequi nesciunt.</p>
  <div class="abs btn-small" style="left:475px;top:803px">Read More</div>
</section>

<section>
  <div class="abs card-photo" style="left:70px;width:236px;background:linear-gradient(180deg,#cfe0ea 0%,#9cb88a 45%,#5f8a3c 100%)" role="img" aria-label="Young goalkeeper celebrating in front of a goal"></div>
  <h3 class="abs card-title" style="left:70px">Upcoming Events</h3>
  <p class="abs card-text" style="left:70px">perspiciatis unde omnis iste natus error sit tot am rem aperiam, eaque ipsa quae ab illo inventore verit atis et quasi architecto beatae vitae dicta sunt explicabo.</p>
  <div class="abs btn-small" style="left:120px;top:1096px">Read More <svg viewBox="0 0 12 12"><circle cx="6" cy="6" r="6" fill="#fff"/><path d="M5 3.5 7.5 6 5 8.5" stroke="#2d4a1b" stroke-width="1.6" fill="none"/></svg></div>

  <div class="abs card-photo" style="left:336px;width:235px;background:linear-gradient(180deg,#e4eef3 0%,#b7cfa5 50%,#6f9a44 100%)" role="img" aria-label="Boy kicking a soccer ball in a park"></div>
  <h3 class="abs card-title" style="left:335px">Previous Events</h3>
  <p class="abs card-text" style="left:335px">perspiciatis unde omnis iste natus error sit tot am rem aperiam, eaque ipsa quae ab illo inventore verit atis et quasi architecto beatae vitae dicta sunt explicabo.</p>
  <div class="abs btn-small" style="left:406px;top:1096px">Read More <svg viewBox="0 0 12 12"><circle cx="6" cy="6" r="6" fill="#fff"/><path d="M5 3.5 7.5 6 5 8.5" stroke="#2d4a1b" stroke-width="1.6" fill="none"/></svg></div>

  <div class="abs card-photo" style="left:598px;width:236px;background:linear-gradient(135deg,#5a3524 0%,#9a6a4c 45%,#3a2418 100%)" role="img" aria-label="Many hands reaching together to hold food"></div>
  <h3 class="abs card-title" style="left:600px">Packages Delivered</h3>
  <p class="abs card-text" style="left:600px">perspiciatis unde omnis iste natus error sit tot am rem aperiam, eaque ipsa quae ab illo inventore verit atis et quasi architecto beatae vitae dicta sunt explicabo.</p>
  <div class="abs btn-small" style="left:663px;top:1096px">Read More <svg viewBox="0 0 12 12"><circle cx="6" cy="6" r="6" fill="#fff"/><path d="M5 3.5 7.5 6 5 8.5" stroke="#2d4a1b" stroke-width="1.6" fill="none"/></svg></div>
</section>

<footer class="abs footer">
  <span class="copy">Copyrights © 2014 companyname.com - All Rights Reserved</span>
  <span class="links">Privacy Policy &nbsp;|&nbsp; Terms Of Uses</span>
</footer>

</body>
</html>
```